Design the Mobile Version of Existing Web Based Health Platform

Loomcrest is a social business enterprise that focus on public health by applying innovative healthcare services and consumer internet technology. Loomcrest offers a personalized platform of health promotion and disease prevention that puts the individual back in control of his life.

Loomcrest is looking for a Mobile Web UX/Visual Design professional to create a mobile version of Loomcrest website platform for iPhone, iPad/tablet and Android.

Contestants must to check www.loomcrest-demo.com.br to have a better understanding of Loomcrest Platform by creating an account (it's in portuguese, but anyone can get the general idea).

The mobile version of Loomcrest should have very similar functionality and user flows. This job is not to reengineer or re-imagine Loomcrest. It is just to reformat the existing functionality so it works well on mobile devices.

This description below is to help you to understand the core features of the platform (check the attachments to see the new web design of each one):

- Personally Controlled Health Record - PCHR enables an individual to own and manage a complete, secure, digital copy of her health and wellness information.
- Health Risk Assessments - is a process to estimate the nature and probability of adverse health effects, based on personal and family historical data, behavior and environment.
- Simulation of future health - "what if analysis" that emphasizes health education and behavior change.
- Step Quests - a program that gives you the opportunity to the participant to advance his personal well-being by doing simple Step Quests
- Health Alerts and Recommendations and Missing Data - Recommendations based on Wellbeing Bureau Guidelines and Federal Wellness Review Panel (FWRP), plus notifications to update outdated information.

The deliverable for this project is a psd file with a designed mobile version of Loomcrest.

A new design of the web platform is under construction. You can also check it looking at the files attached.

Target Market(s)

people 25-40 years old, 60% female, socially engaged

Industry/Entity Type

Healthcare

Requirements
Must have
• iPhone, iPad and Android version

Design must cover all current functionalities available on the web version (please, ensure you understand all features by creating an account at www.loomcrest-demo.com.br)

- Login/Sign up
- Welcome (first assessment)
- Add to Personal Controlled Health Record (PCHR)
- Update/Remove PCHR
- List PCHR
- Riskgrid (risk assessmen results)
- Simulation
- Alerts
- Missing data
- Recommendations
- StepQuest
- Badges
- Configurations

It's important to check the attachments to see how the web platform design is evolving.

```html
<!DOCTYPE html>
<html lang="pt">
<head>
<meta charset="utf-8">
<title>Loomcrest – Cadastro</title>
<link rel="stylesheet" href="https://fonts.googleapis.com/css2?family=Open+Sans:wght@400;600;700&display=swap">
<style>
:root{
  --bg:#f3f3f3;
  --white:#ffffff;
  --orange:#f7902f;
  --orange-dark:#e97a22;
  --orange-bar:#f68c3c;
  --green:#8dc63f;
  --grey-card:#787878;
  --grey-text:#555555;
  --grey-light:#8a8a8a;
  --line:#d6d6d6;
  --blue:#3d9ad6;
  --error:#f08d80;
  --tab-bg:#ebebeb;
  --icon:#8c8c8c;
}
*{box-sizing:border-box;margin:0;padding:0}
html,body{width:1200px;height:2829px;overflow:hidden;background:var(--bg)}
body{position:relative;font-family:"Open Sans",Arial,sans-serif;color:var(--grey-text)}
.abs{position:absolute}

.app-header{left:0;top:0;width:1200px;height:137px;background:var(--white);border-bottom:2px solid var(--line)}
.avatar{left:16px;top:16px;width:114px;height:114px;background:linear-gradient(160deg,#6fa9d6,#3c4a5a)}
.avatar-caret{left:136px;top:60px}
.divider{top:0;width:2px;height:137px;background:var(--line)}
.brand{left:188px;width:878px;top:0;height:137px;display:flex;justify-content:center;align-items:center}
.brand-name{font-weight:700;font-size:72px;color:var(--grey-text);line-height:1}
.menu-icon{left:1100px;top:36px}

.record-bar{left:0;top:137px;width:1200px;height:110px;background:var(--orange-bar)}
.record-icon{left:108px;top:164px}
.record-input{left:181px;top:160px;width:686px;height:64px;background:var(--white);border:2px solid #f2c9a0;font-size:30px;font-weight:600;color:#c2c2c2;padding:10px 22px}
.sponsor{left:900px;top:137px;width:220px;height:110px;display:flex;align-items:center;justify-content:center;font-size:26px;font-weight:700;color:var(--white);white-space:nowrap}

.question{left:146px;top:328px;font-size:26px;color:var(--grey-text)}
.option{top:391px;width:266px;height:267px;background:var(--grey-card);color:var(--white);font-weight:700;font-size:27px;line-height:1.3;display:flex;align-items:center;justify-content:center;text-align:center;padding:20px}
.option--active{background:linear-gradient(135deg,var(--orange-dark),#f6a24f)}
.option-frame{left:764px;top:379px;width:294px;height:293px;border:2px solid var(--orange)}
.tooltip{left:137px;top:702px;width:914px;height:132px;background:var(--white);border:2px solid var(--blue);border-radius:10px;color:var(--blue);font-size:21px;line-height:1.3;text-align:center;padding:12px 20px}
.tooltip-arrow{left:887px;top:680px}

.field-label{left:152px;font-size:30px;font-weight:700;color:var(--grey-text)}
.field-input{left:146px;width:908px;height:71px;background:var(--white);border:2px solid var(--line);border-radius:4px}
.field-input--error{border:3px solid var(--error);box-shadow:0 0 10px rgba(240,141,128,.45)}

.gender{left:146px;top:1431px;width:431px;height:68px;display:flex;border:2px solid var(--line)}
.gender-option{flex:1;display:flex;align-items:center;justify-content:center;font-size:29px;font-weight:700;color:var(--grey-light);background:var(--white)}
.gender-option--on{background:var(--green);color:var(--white)}

.abroad{left:815px;top:1568px;display:flex;align-items:center;gap:14px;font-size:24px;color:var(--grey-text)}
.abroad-box{width:32px;height:32px;background:var(--white);border:2px solid var(--line)}

.select{left:146px;top:2442px;width:464px;height:71px;background:var(--white);border:2px solid var(--line);border-radius:4px}
.select-caret{left:552px;top:2468px}

.next-btn{left:321px;top:2590px;width:594px;height:71px;background:var(--orange);border:2px solid var(--orange-dark);color:var(--white);font-size:30px;font-weight:700;display:flex;align-items:center;justify-content:center}

.tab-bar{left:0;top:2711px;width:1200px;height:118px;background:var(--tab-bg);border-top:2px solid var(--line)}
.tab{top:2735px}
</style>
</head>
<body>

<header class="app-header abs"></header>
<div class="avatar abs" role="img" aria-label="Foto de perfil do usuário"></div>
<svg class="avatar-caret abs" width="36" height="22" viewBox="0 0 36 22"><path d="M2 2 L18 18 L34 2" fill="none" stroke="#666" stroke-width="6"/></svg>
<div class="divider abs" style="left:188px"></div>
<div class="divider abs" style="left:1066px"></div>
<div class="brand abs"><span class="brand-name">Loomcrest</span></div>
<svg class="menu-icon abs" width="68" height="66" viewBox="0 0 68 66">
  <rect x="0" y="0" width="68" height="14" rx="7" fill="#777"/>
  <rect x="0" y="26" width="68" height="14" rx="7" fill="#777"/>
  <rect x="0" y="52" width="68" height="14" rx="7" fill="#777"/>
</svg>

<div class="record-bar abs"></div>
<svg class="record-icon abs" width="46" height="58" viewBox="0 0 46 58">
  <rect x="3" y="7" width="40" height="48" rx="5" fill="none" stroke="#fff" stroke-width="5"/>
  <rect x="14" y="2" width="18" height="10" rx="3" fill="#fff"/>
  <rect x="11" y="22" width="24" height="4" fill="#fff"/>
  <rect x="11" y="32" width="24" height="4" fill="#fff"/>
  <rect x="11" y="42" width="24" height="4" fill="#fff"/>
</svg>
<div class="record-input abs">Add a new record</div>
<div class="sponsor abs">Halvern Pharma</div>

<p class="question abs">Como quer utilizar o Loomcrest?</p>
<div class="option abs" style="left:146px">Vou usar<br>meu CrestPass!</div>
<div class="option abs" style="left:462px">Quero cuidar da minha saúde e posso colaborar com o programa</div>
<div class="option-frame abs"></div>
<div class="option option--active abs" style="left:778px">Quero cuidar da minha saúde, mas não posso pagar nada</div>

<div class="tooltip abs">Promover pequenas mudanças no seu estilo de vida pode ter um efeito global muito positivo em sua vida, sem que você se sinta sobrecarregado com isso.<br>Quem consegue adotar um novo hábito saudável tem mais facilidade para mudar outras práticas, criando um ciclo positivo.</div>
<svg class="tooltip-arrow abs" width="40" height="24" viewBox="0 0 40 24"><path d="M0 23 L20 2 L40 23" fill="#fff" stroke="#3d9ad6" stroke-width="2.5"/></svg>

<label class="field-label abs" style="top:873px">Name</label>
<div class="field-input field-input--error abs" style="top:922px"></div>

<label class="field-label abs" style="top:1038px">Sobrenome</label>
<div class="field-input abs" style="top:1080px"></div>

<label class="field-label abs" style="top:1203px">Data de nascimento</label>
<div class="field-input abs" style="top:1245px"></div>

<label class="field-label abs" style="top:1378px">Sexo</label>
<div class="gender abs"><span class="gender-option gender-option--on">Male</span><span class="gender-option">Female</span></div>

<label class="field-label abs" style="top:1566px">CEP</label>
<div class="abroad abs"><span class="abroad-box"></span>Não moro no Brasil</div>
<div class="field-input abs" style="top:1619px"></div>

<label class="field-label abs" style="top:1734px">Estado</label>
<div class="field-input abs" style="top:1775px"></div>

<label class="field-label abs" style="top:1896px">Cidade</label>
<div class="field-input abs" style="top:1942px"></div>

<label class="field-label abs" style="top:2061px">Endereço</label>
<div class="field-input abs" style="top:2107px"></div>

<label class="field-label abs" style="top:2226px">Bairro</label>
<div class="field-input abs" style="top:2267px"></div>

<label class="field-label abs" style="top:2391px">Etnia</label>
<div class="select abs"></div>
<svg class="select-caret abs" width="28" height="18" viewBox="0 0 28 18"><path d="M0 0 H28 L14 18 Z" fill="#c4c4c4"/></svg>

<div class="next-btn abs">Next</div>

<nav class="tab-bar abs"></nav>
<svg class="tab abs" style="left:108px" width="76" height="72" viewBox="0 0 76 72" fill="#8c8c8c">
  <rect x="0" y="0" width="22" height="22"/><rect x="27" y="0" width="22" height="22"/><rect x="54" y="0" width="22" height="22"/>
  <rect x="0" y="27" width="22" height="22"/><rect x="27" y="27" width="49" height="22"/>
  <rect x="0" y="54" width="49" height="18"/><rect x="54" y="54" width="22" height="18"/>
</svg>
<svg class="tab abs" style="left:328px" width="96" height="86" viewBox="0 0 96 86">
  <path d="M38 4 L2 68 H74 Z" fill="#8c8c8c"/>
  <rect x="34" y="24" width="8" height="26" fill="#ebebeb"/><rect x="34" y="55" width="8" height="8" fill="#ebebeb"/>
  <circle cx="72" cy="66" r="19" fill="#f7902f" stroke="#fff" stroke-width="3"/>
  <text x="72" y="74" font-family="Open Sans,sans-serif" font-size="22" font-weight="700" fill="#fff" text-anchor="middle">15</text>
</svg>
<svg class="tab abs" style="left:562px" width="76" height="64" viewBox="0 0 76 64">
  <rect x="2" y="8" width="72" height="54" fill="#8c8c8c"/>
  <path d="M2 8 L38 38 L74 8" fill="none" stroke="#ebebeb" stroke-width="5"/>
  <rect x="20" y="0" width="36" height="22" fill="#ebebeb" stroke="#8c8c8c" stroke-width="3"/>
</svg>
<svg class="tab abs" style="left:782px" width="84" height="70" viewBox="0 0 84 70">
  <ellipse cx="36" cy="28" rx="34" ry="24" fill="#8c8c8c"/>
  <path d="M12 44 L6 62 L28 50 Z" fill="#8c8c8c"/>
  <ellipse cx="54" cy="40" rx="28" ry="20" fill="#9e9e9e" stroke="#ebebeb" stroke-width="3"/>
  <circle cx="42" cy="40" r="4" fill="#ebebeb"/><circle cx="54" cy="40" r="4" fill="#ebebeb"/><circle cx="66" cy="40" r="4" fill="#ebebeb"/>
</svg>
<svg class="tab abs" style="left:1014px" width="70" height="70" viewBox="0 0 70 70">
  <circle cx="35" cy="35" r="34" fill="#8c8c8c"/>
  <text x="35" y="50" font-family="Open Sans,sans-serif" font-size="42" font-weight="700" fill="#ebebeb" text-anchor="middle">?</text>
</svg>

</body>
</html>
```